Modern Real Estate Sign For Realtor

We need to real estate sign 24x36 or (24x30 if it fits better) Sign that will be attached to a post at homes that are for sale. I like the style of the Meridian 40 yard signs I attached and PD sign with the white trim around it. I Also attached my business card with my logo and name. I would like a black sign with white writing.  I would also like to see options with my headshot included on the sign, either centered or on the right side. The following text should go on the sign:
Logo at the top.
Marcus Hollet
555.317.2096
Marcus@MHolletHomes.example

Requirements
Must have
- Logo at the top.
- Marcus Hollet
- 555.317.2096
- Marcus@MHolletHomes.example

Nice to have
- Headshot open to different design options for how it will be placed on the sign.
- MHolletHomes.example

```html
<!DOCTYPE html>
<html lang="en">
<head>
<meta charset="utf-8">
<title>Hollet Homes Yard Sign</title>
<link rel="stylesheet" href="https://fonts.googleapis.com/css2?family=Oswald:wght@500&family=Roboto+Condensed:wght@700&display=swap">
<style>
  :root {
    --sign-black: #000000;
    --sign-white: #ffffff;
    --backdrop: #e6e6e6;
  }
  * { margin: 0; padding: 0; box-sizing: border-box; }
  html, body {
    width: 904px;
    height: 1200px;
    overflow: hidden;
    background: var(--backdrop);
  }
  .canvas {
    position: relative;
    width: 904px;
    height: 1200px;
  }
  .sign {
    position: absolute;
    left: 92px;
    top: 60px;
    width: 720px;
    height: 1080px;
    background: var(--sign-white);
    overflow: hidden;
  }
  .sign-shapes {
    position: absolute;
    inset: 0;
  }
  .brand {
    position: absolute;
    top: 150px;
    left: 0;
    width: 100%;
    display: flex;
    justify-content: center;
    align-items: center;
    gap: 16px;
  }
  .brand-mark {
    width: 34px;
    height: 34px;
    background: var(--sign-white);
  }
  .brand-name {
    font-family: "Roboto Condensed", sans-serif;
    font-weight: 700;
    font-size: 48px;
    line-height: 1;
    color: var(--sign-white);
  }
  .agent-name {
    position: absolute;
    top: 325px;
    left: 0;
    width: 100%;
    text-align: center;
    font-family: "Roboto Condensed", sans-serif;
    font-weight: 700;
    font-size: 76px;
    line-height: 1.2;
    color: var(--sign-white);
  }
  .agent-phone {
    position: absolute;
    top: 640px;
    left: 0;
    width: 100%;
    text-align: center;
    font-family: "Oswald", sans-serif;
    font-weight: 500;
    font-size: 118px;
    line-height: 1;
    letter-spacing: -2px;
    color: var(--sign-black);
  }
  .contact-band {
    position: absolute;
    left: 0;
    bottom: 0;
    width: 100%;
    height: 225px;
    background: var(--sign-black);
  }
  .agent-email {
    position: absolute;
    top: 92px;
    left: 0;
    width: 100%;
    text-align: center;
    font-family: "Roboto Condensed", sans-serif;
    font-weight: 700;
    font-size: 36px;
    line-height: 1.2;
    color: var(--sign-white);
  }
</style>
</head>
<body>
  <main class="canvas">
    <section class="sign">
      <svg class="sign-shapes" width="720" height="1080" viewBox="0 0 720 1080" aria-hidden="true">
        <polygon class="header-chevron" points="0,0 720,0 720,430 360,555 0,430" fill="var(--sign-black)"/>
        <polygon class="chevron-trim" points="0,446 360,571 720,446 720,454 360,583 0,454" fill="var(--sign-black)"/>
      </svg>
      <div class="brand">
        <span class="brand-mark"></span>
        <span class="brand-name">Hollet Homes</span>
      </div>
      <h1 class="agent-name">Marcus Hollet</h1>
      <p class="agent-phone">555.317.2096</p>
      <div class="contact-band">
        <p class="agent-email">Marcus@MHolletHomes.example</p>
      </div>
    </section>
  </main>
</body>
</html>
```